Business Cards

Business card design for my company.
I would like the card's background colour to be black. You can also see our web site to get an idea of our brand. https://www.dlqmarrowfield.com.au/
- Name
- Email

```html
<!DOCTYPE html>
<html lang="en">
<head>
<meta charset="utf-8">
<title>DLQ Marrowfield – Business Card</title>
<link rel="stylesheet" href="https://fonts.googleapis.com/css2?family=Barlow:ital,wght@0,700;1,800&family=Roboto:wght@300;400&display=swap">
<style>
  :root {
    --ink: #000000;
    --paper: #f2f2f2;
    --page: #ffffff;
    --green: #0a9447;
    --green-bright: #10b04f;
    --green-dark: #1f5a36;
    --white: #ffffff;
  }
  * { margin: 0; padding: 0; box-sizing: border-box; }
  html, body {
    width: 1200px;
    height: 785px;
    overflow: hidden;
    background: var(--page);
  }
  .card {
    position: absolute;
    left: 297.6px;
    width: 604.8px;
    height: 345.6px;
    overflow: hidden;
  }
  .card--front { top: 42.4px; background: var(--paper); }
  .card--back  { top: 396px;  background: var(--ink); }

  .card__shapes {
    position: absolute;
    inset: 0;
    width: 100%;
    height: 100%;
  }

  .brand {
    position: absolute;
    display: flex;
    align-items: center;
    font-family: "Barlow", sans-serif;
    font-weight: 700;
    white-space: nowrap;
    line-height: 1;
  }
  .brand__square {
    display: block;
    flex: none;
    background: var(--green);
  }
  .brand--front {
    left: 40px;
    top: 178px;
    gap: 7px;
    font-size: 23px;
    color: var(--ink);
  }
  .brand--front .brand__square { width: 13px; height: 13px; }
  .brand--back {
    left: 50%;
    top: 172.8px;
    transform: translate(-50%, -50%);
    gap: 12px;
    font-size: 38px;
    color: var(--white);
  }
  .brand--back .brand__square { width: 20px; height: 20px; }

  .holder {
    position: absolute;
    right: 34.4px;
    top: 100px;
    text-align: right;
  }
  .holder__name {
    font-family: "Barlow", sans-serif;
    font-style: italic;
    font-weight: 800;
    font-size: 37px;
    line-height: 42px;
    letter-spacing: 0.5px;
    text-transform: uppercase;
    color: var(--ink);
  }
  .holder__role {
    font-family: "Roboto", sans-serif;
    font-weight: 400;
    font-size: 16.5px;
    line-height: 20px;
    color: var(--ink);
  }
  .holder__rule {
    display: block;
    width: 120px;
    height: 2.4px;
    margin: 8px 1px 0 auto;
    background: var(--green);
  }

  .contact {
    position: absolute;
    right: 35px;
    top: 223px;
    text-align: right;
    list-style: none;
    font-family: "Roboto", sans-serif;
    font-weight: 300;
    font-size: 16.5px;
    line-height: 20.5px;
    color: var(--ink);
  }
</style>
</head>
<body>

  <section class="card card--front" aria-label="Card front">
    <svg class="card__shapes" viewBox="0 0 604.8 345.6" aria-hidden="true">
      <defs>
        <linearGradient id="stripeGradient" x1="0" y1="0" x2="1" y2="0">
          <stop offset="0" stop-color="var(--green-dark)"/>
          <stop offset="1" stop-color="var(--green-bright)"/>
        </linearGradient>
      </defs>
      <polygon class="wedge-left" points="0,0 48,0 0,189.6" fill="var(--ink)"/>
      <polygon class="accent-stripe" points="297.6,0 323.2,0 235.2,345.6 209.6,345.6" fill="url(#stripeGradient)"/>
      <polygon class="wedge-right" points="604.8,173.6 604.8,345.6 560.8,345.6" fill="var(--ink)"/>
    </svg>

    <div class="brand brand--front">
      <span class="brand__square"></span>
      <span class="brand__name">DLQ Marrowfield</span>
    </div>

    <div class="holder">
      <h1 class="holder__name">Dean<br>Halvorsen</h1>
      <p class="holder__role">General Manager</p>
      <span class="holder__rule"></span>
    </div>

    <ul class="contact">
      <li class="contact__phone">0400 123 456</li>
      <li class="contact__email">info@dlqmarrowfield.com.au</li>
      <li class="contact__web">https://www.dlqmarrowfield.com.au/</li>
    </ul>
  </section>

  <section class="card card--back" aria-label="Card back">
    <div class="brand brand--back">
      <span class="brand__square"></span>
      <span class="brand__name">DLQ Marrowfield</span>
    </div>
  </section>

</body>
</html>
```